Zuvo Decor

There is a sample provided with the arabic text of the business card. please copy paste the same text and the same Logo (The two triangles) Just try to incorproate the Brown background attached (you are free to change the colors) Id like the colors to be mainly shades of black and red.

```html
<!DOCTYPE html>
<html lang="ar">
<head>
<meta charset="utf-8">
<title>Zuvo Decor – Business Cards</title>
<link rel="stylesheet" href="https://fonts.googleapis.com/css2?family=Tajawal:wght@400;500;700&family=Aref+Ruqaa:wght@700&family=Roboto:wght@500&display=swap">
<style>
  :root {
    --bg: #2b2b2c;
    --card: #1b1b1c;
    --red: #e60000;
    --white: #f2f2f2;
    --muted: #3a3a3c;
  }
  * { margin: 0; padding: 0; box-sizing: border-box; }
  html, body { width: 1200px; height: 1138px; overflow: hidden; }
  body { background: var(--bg); position: relative; font-family: "Tajawal", sans-serif; }

  .card {
    position: absolute;
    left: 276px;
    width: 620px;
    height: 374px;
    background: var(--card);
    border-radius: 14px;
    overflow: hidden;
    box-shadow: 0 10px 24px rgba(0,0,0,.45);
  }
  .card--front { top: 186px; }
  .card--back { top: 608px; }

  /* Front */
  .brand-panel {
    position: absolute;
    left: 0; top: 26px;
    width: 285px; height: 326px;
    background: linear-gradient(135deg, #141414 0%, #1f1f20 60%, #2a2a2b 100%);
    display: flex; align-items: center; justify-content: center;
  }
  .brand-panel__name {
    font-weight: 700;
    font-size: 40px;
    color: var(--muted);
    letter-spacing: 1px;
  }
  .credentials {
    position: absolute;
    right: 62px; top: 65px;
    direction: rtl;
    list-style: none;
  }
  .credentials li {
    display: flex; align-items: center; gap: 18px;
    height: 30.4px;
    font-size: 20px;
    line-height: 1;
    color: var(--white);
    white-space: nowrap;
  }
  .credentials .tick { width: 18px; height: 18px; flex: none; }

  /* Back */
  .red-wedge { position: absolute; left: 0; top: 0; width: 620px; height: 374px; }
  .owner {
    position: absolute;
    right: 394px; top: 30px;
    direction: rtl; text-align: right;
    white-space: nowrap;
  }
  .owner__name {
    font-family: "Aref Ruqaa", serif;
    font-weight: 700;
    font-size: 26px;
    color: var(--white);
    line-height: 1.3;
  }
  .owner__title {
    font-family: "Aref Ruqaa", serif;
    font-weight: 700;
    font-size: 16px;
    color: var(--red);
    margin-right: 62px;
    line-height: 1.3;
  }
  .back-credentials {
    position: absolute;
    right: 367px; top: 150px;
    direction: rtl; list-style: none;
  }
  .back-credentials li {
    height: 34px;
    font-size: 20px;
    color: var(--white);
    white-space: nowrap;
  }
  .divider {
    position: absolute;
    left: 0; top: 311px;
    width: 428px; height: 2px;
    background: var(--red);
  }
  .contact {
    position: absolute;
    left: 36px; top: 326px;
    display: flex; align-items: center; gap: 16px;
  }
  .contact__icon { width: 30px; height: 30px; }
  .contact__phone {
    font-family: "Roboto", sans-serif;
    font-weight: 500;
    font-size: 24px;
    color: var(--white);
  }
  .brand-name {
    position: absolute;
    left: 509px; top: 170px;
    transform: translate(-50%, -50%);
    font-weight: 700;
    font-size: 34px;
    color: var(--white);
    white-space: nowrap;
  }
</style>
</head>
<body>

<section class="card card--front">
  <div class="brand-panel" role="img" aria-label="Zuvo Decor brand area">
    <span class="brand-panel__name">Zuvo Decor</span>
  </div>
  <ul class="credentials">
    <li><svg class="tick" viewBox="0 0 18 18"><path d="M3 9.5l4 4 8-9" fill="none" stroke="#e60000" stroke-width="2.2"/></svg>ماجســــتير هندسة ديكور</li>
    <li><svg class="tick" viewBox="0 0 18 18"><path d="M3 9.5l4 4 8-9" fill="none" stroke="#e60000" stroke-width="2.2"/></svg>دبلوم عالي فن تشـــكيلي</li>
    <li><svg class="tick" viewBox="0 0 18 18"><path d="M3 9.5l4 4 8-9" fill="none" stroke="#e60000" stroke-width="2.2"/></svg>أكاديمية الـــفنون (نوران)</li>
    <li><svg class="tick" viewBox="0 0 18 18"><path d="M3 9.5l4 4 8-9" fill="none" stroke="#e60000" stroke-width="2.2"/></svg>استشارات هندسية - فنية</li>
    <li><svg class="tick" viewBox="0 0 18 18"><path d="M3 9.5l4 4 8-9" fill="none" stroke="#e60000" stroke-width="2.2"/></svg>ماجســــتير هندسة ديكور</li>
    <li><svg class="tick" viewBox="0 0 18 18"><path d="M3 9.5l4 4 8-9" fill="none" stroke="#e60000" stroke-width="2.2"/></svg>دبلوم عالي فن تشـــكيلي</li>
    <li><svg class="tick" viewBox="0 0 18 18"><path d="M3 9.5l4 4 8-9" fill="none" stroke="#e60000" stroke-width="2.2"/></svg>أكاديمية الـــفنون (نوران)</li>
    <li><svg class="tick" viewBox="0 0 18 18"><path d="M3 9.5l4 4 8-9" fill="none" stroke="#e60000" stroke-width="2.2"/></svg>استشارات هندسية - فنية</li>
  </ul>
</section>

<section class="card card--back">
  <svg class="red-wedge" viewBox="0 0 620 374" aria-hidden="true">
    <defs>
      <linearGradient id="wedgeRed" x1="0" y1="0" x2="0" y2="1">
        <stop offset="0" stop-color="#ee0000"/>
        <stop offset="1" stop-color="#d40000"/>
      </linearGradient>
    </defs>
    <polygon points="300,0 620,0 620,374 450,374" fill="url(#wedgeRed)"/>
  </svg>

  <div class="owner">
    <div class="owner__name">المهندس / سامر نادر الفارس</div>
    <div class="owner__title">أستاذ جامعي</div>
  </div>

  <ul class="back-credentials">
    <li>ماجســــتير هندسة ديكور</li>
    <li>دبلوم عالي فن تشـــكيلي</li>
    <li>أكاديمية الـــفنون (نوران)</li>
    <li>استشارات هندسية -فنية</li>
  </ul>

  <div class="divider"></div>

  <div class="contact">
    <svg class="contact__icon" viewBox="0 0 30 30" aria-hidden="true">
      <circle cx="15" cy="15" r="13.5" fill="none" stroke="#e60000" stroke-width="1.8"/>
      <path d="M10 20c3 3 7 3 9 1l1.5-1.5-3-3-1.5 1.5c-1.5-.5-3-2-3.5-3.5L14 13l-3-3-1.5 1.5c-2 2-2 6 .5 8.5z" fill="none" stroke="#e60000" stroke-width="1.6" stroke-linejoin="round"/>
    </svg>
    <span class="contact__phone">31245067/65558120</span>
  </div>

  <div class="brand-name">Zuvo Decor</div>
</section>

</body>
</html>
```